Brevanta Interiors
Business Card, Stationery Package, Email Signature
Project: Brevanta Interiors
Brevanta Interiors -
Creative Brief
Professional
Marisol Pryde
Managing Director
P.O.Box 4372 Converse, TX 78109 - 4372
mpryde@brevantainteriors.example
www.brevantainteriors.example
Brevanta Interiors is a retail store offering Flooring products and Installation services. We would like to have the following items made: Business Card, Stationery Package (Fax, Letterhead, Envelopes, etc.), and Email Signature. We would like to see two types of fonts created for comparison, the original font and one of your own professional choices. Winner, please provide all design templates for future modification upon completion of the contest. Thank you!
logo, text, slogan, and web address.

```html
<!DOCTYPE html>
<html lang="en">
<head>
<meta charset="utf-8">
<title>Brevanta Interiors — Stationery Package</title>
<link href="https://fonts.googleapis.com/css2?family=Open+Sans:wght@400;600;700&display=swap" rel="stylesheet">
<style>
  :root{
    --bg:#efeae4;
    --paper:#ffffff;
    --ink:#2b2b2b;
    --muted:#777;
    --blue:#1d5fae;
    --green:#3d9e3a;
    --dark:#111111;
    --faint:#e8ebf0;
    --line:#555;
  }
  *{box-sizing:border-box;margin:0;padding:0}
  html,body{width:1200px;height:434px;overflow:hidden}
  body{background:var(--bg);font-family:"Open Sans",Arial,sans-serif;color:var(--ink);position:relative}
  .piece{position:absolute;background:var(--paper);box-shadow:0 2px 6px rgba(0,0,0,.18);overflow:hidden}
  .swoosh{position:absolute;top:0;right:0}
  .brand{font-weight:700;color:var(--blue);white-space:nowrap;line-height:1;display:flex;align-items:center;gap:4px}
  .brand .dot{display:inline-block;background:var(--green);border-radius:50%;flex:none}
  .brand.on-dark{color:#fff}
  .contact{font-size:5px;line-height:1.5;color:var(--muted);white-space:nowrap}
  .watermark{position:absolute;left:0;right:0;text-align:center;color:var(--faint);font-weight:700;white-space:nowrap;line-height:1}

  /* left envelope front */
  .envelope-front{left:41px;top:48px;width:295px;height:106px}
  .envelope-front .brand{position:absolute;left:10px;top:14px;font-size:10px}
  .envelope-front .name{position:absolute;left:120px;top:10px;font-size:6px;font-weight:600;color:var(--ink)}
  .envelope-front .sender{position:absolute;left:10px;top:30px;font-size:4.5px}

  /* left envelope back */
  .envelope-back{left:41px;top:163px;width:295px;height:173px}
  .envelope-back .flap{position:absolute;left:0;top:0}
  .envelope-back .seal{position:absolute;left:0;right:0;top:52px;justify-content:center;font-size:8px}
  .envelope-back .band{position:absolute;left:0;right:0;top:106px;height:43px;background:var(--dark);display:flex;align-items:center;justify-content:center}
  .envelope-back .band .brand{font-size:8px}

  /* fax */
  .fax{left:336px;top:36px;width:259px;height:348px}
  .fax .brand{position:absolute;left:12px;top:16px;font-size:10px}
  .fax .sender{position:absolute;left:148px;top:10px;font-size:4.5px}
  .fax .title{position:absolute;right:14px;top:60px;font-size:11px;font-weight:700;color:var(--ink)}
  .fax table{position:absolute;left:12px;top:76px;width:235px;border-collapse:collapse;font-size:5px}
  .fax td{border:1px solid var(--line);height:12px;padding:0 3px;width:50%}
  .fax .options{position:absolute;left:12px;top:138px;width:235px;display:flex;justify-content:space-between;font-size:4.5px}
  .fax .options span::before{content:"";display:inline-block;width:5px;height:5px;border:1px solid var(--line);margin-right:2px;vertical-align:-1px}
  .fax .watermark{top:222px;font-size:32px}

  /* letterhead */
  .letterhead{left:610px;top:36px;width:259px;height:348px}
  .letterhead .brand{position:absolute;left:12px;top:16px;font-size:10px}
  .letterhead .sender{position:absolute;left:148px;top:10px;font-size:4.5px}
  .letterhead .watermark{top:186px;font-size:32px}

  /* cards */
  .card-front{left:970px;top:77px;width:122px;height:48px}
  .card-front .brand{position:absolute;left:6px;top:9px;font-size:7px}
  .card-front .tag{position:absolute;left:6px;top:20px;font-size:3.5px;color:var(--green);letter-spacing:.3px}
  .card-front .person{position:absolute;left:6px;top:28px;font-size:3.5px;line-height:1.5;color:var(--muted)}
  .card-back{left:902px;top:144px;width:104px;height:48px;background:var(--dark);display:flex;align-items:center;justify-content:center}
  .card-back .brand{font-size:7px}
  .card-alt{left:1037px;top:144px;width:113px;height:48px;display:flex;align-items:center;justify-content:center}
  .card-alt .brand{font-size:7px}

  /* right envelope */
  .envelope-right{left:886px;top:223px;width:273px;height:132px}
  .envelope-right .brand{position:absolute;left:10px;top:14px;font-size:9px}
  .envelope-right .sender{position:absolute;left:10px;top:28px;font-size:4.5px}
  .envelope-right .watermark{left:auto;right:14px;top:50px;font-size:26px}
</style>
</head>
<body>

  <div class="piece envelope-front">
    <svg class="swoosh" width="80" height="52" viewBox="0 0 80 52" aria-hidden="true">
      <path d="M18 0 H80 V52 C71 26 49 8 18 0Z" fill="var(--blue)"/>
      <path d="M40 0 H80 V33 C73 16 60 5 40 0Z" fill="var(--green)"/>
    </svg>
    <div class="brand"><span class="dot" style="width:7px;height:7px"></span>Brevanta Interiors</div>
    <div class="name">Marisol Pryde</div>
    <div class="contact sender">Managing Director<br>P.O.Box 4372 Larkhaven, TX 70000 - 0000<br>Phone (210) 555-0148<br>mpryde@brevantainteriors.example</div>
  </div>

  <div class="piece envelope-back">
    <svg class="flap" width="295" height="40" viewBox="0 0 295 40" aria-hidden="true">
      <path d="M0 4 L147 36 L295 4" fill="none" stroke="#ccc" stroke-width="1"/>
    </svg>
    <div class="brand seal">Brevanta Interiors</div>
    <div class="band"><div class="brand on-dark">Brevanta Interiors</div></div>
  </div>

  <div class="piece fax">
    <svg class="swoosh" width="56" height="38" viewBox="0 0 56 38" aria-hidden="true">
      <path d="M10 0 H56 V38 C49 19 34 6 10 0Z" fill="var(--blue)"/>
      <path d="M28 0 H56 V24 C50 11 41 4 28 0Z" fill="var(--green)"/>
    </svg>
    <div class="brand"><span class="dot" style="width:7px;height:7px"></span>Brevanta Interiors</div>
    <div class="contact sender">P.O.Box 4372 Larkhaven, TX 70000 - 0000<br>Phone (210) 555-0148<br>Fax (210) 555-0149<br>mpryde@brevantainteriors.example<br>www.brevantainteriors.example</div>
    <div class="title">FAX</div>
    <table>
      <tr><td>To:</td><td>From:</td></tr>
      <tr><td>Fax:</td><td>Pages:</td></tr>
      <tr><td>Phone:</td><td>Date:</td></tr>
      <tr><td>Re:</td><td>CC:</td></tr>
    </table>
    <div class="options"><span>Urgent</span><span>For Review</span><span>Please Comment</span><span>Please Reply</span><span>Please Recycle</span></div>
    <div class="watermark">Brevanta</div>
  </div>

  <div class="piece letterhead">
    <svg class="swoosh" width="56" height="38" viewBox="0 0 56 38" aria-hidden="true">
      <path d="M10 0 H56 V38 C49 19 34 6 10 0Z" fill="var(--blue)"/>
      <path d="M28 0 H56 V24 C50 11 41 4 28 0Z" fill="var(--green)"/>
    </svg>
    <div class="brand"><span class="dot" style="width:7px;height:7px"></span>Brevanta Interiors</div>
    <div class="contact sender">P.O.Box 4372 Larkhaven, TX 70000 - 0000<br>Phone (210) 555-0148<br>Fax (210) 555-0149<br>mpryde@brevantainteriors.example<br>www.brevantainteriors.example</div>
    <div class="watermark">Brevanta</div>
  </div>

  <div class="piece card-front">
    <svg class="swoosh" width="30" height="22" viewBox="0 0 30 22" aria-hidden="true">
      <path d="M5 0 H30 V22 C26 11 18 4 5 0Z" fill="var(--blue)"/>
      <path d="M15 0 H30 V13 C27 6 22 2 15 0Z" fill="var(--green)"/>
    </svg>
    <div class="brand"><span class="dot" style="width:5px;height:5px"></span>Brevanta Interiors</div>
    <div class="tag">FLOORING &amp; INSTALLATION</div>
    <div class="person">Marisol Pryde, Managing Director<br>mpryde@brevantainteriors.example</div>
  </div>

  <div class="piece card-back"><div class="brand on-dark">Brevanta Interiors</div></div>

  <div class="piece card-alt"><div class="brand">Brevanta Interiors</div></div>

  <div class="piece envelope-right">
    <svg class="swoosh" width="66" height="46" viewBox="0 0 66 46" aria-hidden="true">
      <path d="M13 0 H66 V46 C58 23 40 7 13 0Z" fill="var(--blue)"/>
      <path d="M34 0 H66 V28 C60 14 49 4 34 0Z" fill="var(--green)"/>
    </svg>
    <div class="brand"><span class="dot" style="width:6px;height:6px"></span>Brevanta Interiors</div>
    <div class="contact sender">P.O.Box 4372 Larkhaven, TX 70000 - 0000</div>
    <div class="watermark">Brevanta</div>
  </div>

</body>
</html>
```